Thank you for shopping with us business card

We would like a thank you card for our rebranded business. We used to be "Brindle Goods" but are now "Marlow Finds. Old thank you card and new logo will be attached for reference. New thank you card does not have to be same design as old thank you card, but please use new logo.
Shopmart URL is now marlowfinds.shopmart.example
Instagram is @Marlow_Finds
Email is marlowfinds@mailbox.example
Thank you!

Contact Information for Business Card

Shopmart site, email, Instagram

```html
<!DOCTYPE html>
<html lang="en">
<head>
<meta charset="utf-8">
<title>Marlow Finds – Thank You Card</title>
<link rel="stylesheet" href="https://fonts.googleapis.com/css2?family=Poppins:wght@300;600&display=swap">
<style>
  :root {
    --ink: #000000;
    --paper: #ffffff;
    --backdrop: #e6e6e6;
    --rule: #333333;
  }
  * { box-sizing: border-box; margin: 0; padding: 0; }
  html, body {
    width: 1200px;
    height: 1162px;
    overflow: hidden;
    background: var(--backdrop);
    font-family: "Poppins", sans-serif;
  }
  .sheet {
    width: 1200px;
    height: 1162px;
    display: flex;
    flex-direction: column;
    align-items: center;
    justify-content: center;
    gap: 28px;
  }
  .card {
    width: 960px;
    height: 540px;
    position: relative;
    overflow: hidden;
  }
  /* Front face */
  .card-front {
    background: var(--ink);
    display: flex;
    align-items: center;
    justify-content: center;
  }
  .brand-name {
    color: var(--paper);
    font-weight: 600;
    font-size: 44px;
    letter-spacing: 0.02em;
    text-transform: uppercase;
  }
  /* Back face */
  .card-back {
    background: var(--paper);
    display: flex;
    flex-direction: column;
  }
  .back-header {
    background: var(--ink);
    color: var(--paper);
    height: 245px;
    display: flex;
    flex-direction: column;
    align-items: center;
    justify-content: center;
    text-align: center;
  }
  .heart { width: 42px; height: 38px; margin-bottom: 22px; }
  .thanks-line { font-weight: 300; font-size: 30px; line-height: 1.15; }
  .thanks-name { font-weight: 600; font-size: 28px; line-height: 1.2; }
  .back-body {
    flex: 1;
    display: flex;
    flex-direction: column;
    align-items: center;
    text-align: center;
    color: var(--ink);
    padding-top: 22px;
  }
  .message { font-weight: 300; font-size: 27px; line-height: 1.33; }
  .review { font-weight: 300; font-size: 27px; margin-top: 36px; }
  .divider {
    width: 290px;
    height: 1px;
    background: var(--rule);
    margin-top: 28px;
  }
  .contacts {
    display: flex;
    justify-content: space-between;
    width: 840px;
    margin-top: 14px;
    font-weight: 300;
    font-size: 18px;
  }
  .contact { display: flex; align-items: center; gap: 10px; }
  .contact-mark {
    width: 20px; height: 20px;
    border-radius: 50%;
    background: var(--ink);
    display: inline-flex;
    align-items: center;
    justify-content: center;
    flex-shrink: 0;
  }
  .bottom-band {
    height: 10px;
    background: var(--ink);
  }
</style>
</head>
<body>
<main class="sheet">
  <section class="card card-front" aria-label="Card front">
    <h1 class="brand-name">Marlow Finds</h1>
  </section>

  <section class="card card-back" aria-label="Card back">
    <header class="back-header">
      <svg class="heart" viewBox="0 0 24 22" aria-hidden="true">
        <path fill="#ffffff" d="M12 21.5 10.3 20C4.2 14.5 0 10.7 0 6.2 0 2.6 2.8 0 6.4 0c2.1 0 4.1 1 5.6 2.5C13.5 1 15.5 0 17.6 0 21.2 0 24 2.6 24 6.2c0 4.5-4.2 8.3-10.3 13.8z"/>
      </svg>
      <p class="thanks-line">Thank You for Choosing</p>
      <p class="thanks-name">Marlow Finds!</p>
    </header>
    <div class="back-body">
      <p class="message">Your purchase made my day,<br>and I hope this package brightens yours.<br>Your support means the world to me.</p>
      <p class="review">Please come back and leave a review!</p>
      <div class="divider"></div>
      <ul class="contacts" style="list-style:none">
        <li class="contact"><span class="contact-mark"></span>marlowfinds.shopmart.example</li>
        <li class="contact"><span class="contact-mark"></span>Marlow_Finds</li>
        <li class="contact">
          <span class="contact-mark">
            <svg width="12" height="9" viewBox="0 0 12 9" aria-hidden="true">
              <rect x="0.5" y="0.5" width="11" height="8" fill="none" stroke="#fff"/>
              <path d="M0.5 0.5 6 5l5.5-4.5" fill="none" stroke="#fff"/>
            </svg>
          </span>marlowfinds@mailbox.example
        </li>
      </ul>
    </div>
    <div class="bottom-band"></div>
  </section>
</main>
</body>
</html>
```